Tovin Marsk Technologies Web Site

I need website designed for Tovin Marsk Technologies, LLC. It is an email marketing software as a service business. I am looking for a five page website with the ability to accept payments. I have included our logo below for integration with the website. I do not have the text ready yet.

The domain to use is tovin-marsk.com

I have also included some examples of other websites that outline the basic structure I would like
https://trybluvesto.com/
https://www.postvaro.com/

I know I need to provide some more information, but I want to get the ball rolling and see what is needed.
Thanks!
Eli

```html
<!DOCTYPE html>
<html lang="en">
<head>
<meta charset="utf-8">
<title>Tovin Marsk Technologies</title>
<link href="https://fonts.googleapis.com/css2?family=Poppins:wght@400;500;600;700&family=Karla:wght@400;500;700&display=swap" rel="stylesheet">
<style>
:root{
  --hero:#211b6b;
  --navy:#0e1e4f;
  --blue:#1a5df0;
  --ink:#1c1d3a;
  --muted:#9aa0b6;
  --soft:#f4f6fc;
  --line:#e6e9f2;
  --white:#ffffff;
}
*{margin:0;padding:0;box-sizing:border-box}
html,body{width:1200px;height:4126px;overflow:hidden}
body{position:relative;background:var(--white);font-family:"Karla",sans-serif;color:var(--ink)}
.abs{position:absolute}
h1,h2,h3,h4,.brand,.btn{font-family:"Poppins",sans-serif}

/* hero */
.hero{position:absolute;left:0;top:0;width:1200px;height:710px;background:var(--hero);clip-path:polygon(0 0,100% 0,100% 585px,0 705px)}
.brand{position:absolute;left:62px;top:14px;width:110px;text-align:center;color:#fff;font-size:15px;font-weight:600;letter-spacing:.5px}
.brand-mark{display:block;margin:0 auto 6px;width:44px;height:44px;border-radius:50%;border:3px solid #e24a6c}
.nav-item{position:absolute;top:30px;font:500 13px "Poppins",sans-serif;color:#fff;white-space:nowrap}
.login{position:absolute;left:1013px;top:20px;width:165px;height:38px;border-radius:20px;background:#fff;color:var(--hero);font:500 14px "Poppins",sans-serif;display:flex;align-items:center;justify-content:center;gap:6px}
.hero h1{position:absolute;top:182px;width:1200px;text-align:center;color:#fff;font-size:60px;font-weight:700;line-height:72px}
.hero p{position:absolute;top:340px;left:230px;width:740px;text-align:center;color:#fff;font-size:16px;line-height:30px;font-weight:500}
.ghost{position:absolute;top:435px;height:40px;border:1.5px solid #fff;border-radius:20px;color:#fff;font:500 14px "Poppins",sans-serif;display:flex;align-items:center;justify-content:center}
.down{position:absolute;left:567px;top:617px;width:66px;height:66px;border-radius:50%;background:var(--blue);display:flex;align-items:center;justify-content:center;box-shadow:0 0 0 8px #fff}

/* features */
.feature{position:absolute;top:818px;width:275px}
.feature svg{display:block;height:70px}
.feature h3{margin-top:48px;font-size:17px;font-weight:500}
.feature p{margin-top:22px;font-size:14px;line-height:28px;color:var(--muted)}

/* section heads */
.head{position:absolute;width:1200px;text-align:center}
.head h2{font-size:30px;font-weight:600}
.head .rule{width:50px;height:3px;background:var(--blue);margin:14px auto 20px}
.head p{width:560px;margin:0 auto;font-size:14px;line-height:24px;color:var(--muted)}

/* pricing */
.pricing-bg{position:absolute;left:0;top:1110px;width:1200px;height:820px;background:var(--soft);clip-path:polygon(0 45px,100% 0,100% 770px,0 820px)}
.plan{position:absolute;top:1376px;width:272px;height:476px;background:#fff;box-shadow:0 4px 18px rgba(30,40,90,.08);overflow:hidden;text-align:center}
.plan h4{margin-top:26px;font-size:18px;font-weight:500}
.plan .sub{margin-top:8px;font-size:13px;color:var(--muted)}
.plan .rule{width:50px;height:2px;background:var(--blue);margin:14px auto 0}
.plan ul{list-style:none;text-align:left;padding-left:30px;margin-top:22px}
.plan li{font-size:13px;line-height:30.5px;color:#5a5f77}
.price{position:absolute;left:30px;top:302px;font:600 40px "Poppins",sans-serif;color:var(--ink)}
.price sup{font-size:17px;vertical-align:20px}
.price small{font-size:12px;color:var(--muted);font-weight:400}
.plan .base{position:absolute;left:0;bottom:0}
.buy{position:absolute;left:86px;bottom:30px;width:100px;height:36px;border:1.5px solid #fff;border-radius:18px;color:#fff;font:500 13px "Poppins",sans-serif;display:flex;align-items:center;justify-content:center}
.popular{position:absolute;right:0;top:246px;width:24px;height:120px;background:var(--blue);color:#fff;font:600 11px "Poppins",sans-serif;writing-mode:vertical-rl;transform:rotate(180deg);display:flex;align-items:center;justify-content:center;letter-spacing:1px}

/* why */
.why h2{position:absolute;left:17px;top:2025px;font-size:30px;font-weight:600}
.why .intro{position:absolute;left:17px;top:2096px;width:560px;font-size:14px;line-height:28px;color:var(--muted)}
.point{position:absolute;width:280px}
.point h4{font-size:17px;font-weight:500}
.point p{margin-top:14px;font-size:14px;line-height:28px;color:var(--muted)}
.purchase{position:absolute;left:17px;top:2449px;width:154px;height:40px;border-radius:20px;background:var(--blue);color:#fff;font:500 14px "Poppins",sans-serif;display:flex;align-items:center;justify-content:center}
.video{position:absolute;left:614px;top:2078px;width:567px;height:347px;background:linear-gradient(135deg,#2c3856 0%,#55627e 45%,#8d97ab 70%,#3d4863 100%)}
.video .play{position:absolute;left:253px;top:115px;width:62px;height:62px;border-radius:50%;border:2px solid #fff;display:flex;align-items:center;justify-content:center}
.video span{position:absolute;top:198px;width:567px;text-align:center;color:#fff;font:500 15px "Poppins",sans-serif}

/* clients */
.clients-bg{position:absolute;left:0;top:2590px;width:1200px;height:560px;background:var(--soft);clip-path:polygon(0 70px,100% 0,100% 100%,0 100%)}
.quote{position:absolute;top:2848px;width:368px;height:215px;background:#fff;box-shadow:0 4px 18px rgba(30,40,90,.08);overflow:hidden}
.quote .qmark{position:absolute;left:32px;top:30px;width:58px;height:58px;border-radius:50%;background:var(--soft);color:var(--blue);font:700 30px "Poppins",sans-serif;display:flex;align-items:center;justify-content:center}
.quote h4{position:absolute;left:104px;top:40px;font-size:15px;font-weight:500}
.quote .loc{position:absolute;left:104px;top:66px;font-size:12px;color:var(--muted)}
.quote p{position:absolute;left:32px;top:112px;width:310px;font-size:14px;line-height:22px;color:#4c5168}
.quote svg{position:absolute;left:0;bottom:0}
.dots{position:absolute;left:570px;top:3096px;display:flex;gap:6px}
.dots i{display:block;width:8px;height:6px;border-radius:3px;background:#d3d8e6}
.dots i:first-child{width:14px;background:var(--blue)}

/* newsletter */
.news h2{position:absolute;left:17px;top:3172px;font-size:30px;font-weight:600}
.news p{position:absolute;left:17px;top:3232px;width:660px;font-size:17px;line-height:32px;color:#5a5f77}
.signup{position:absolute;left:715px;top:3212px;width:468px;height:44px;border:1.5px solid var(--blue);border-radius:22px}
.signup span{position:absolute;left:30px;top:12px;font-size:14px;color:#6a6f86}
.signup b{position:absolute;right:4px;top:4px;width:124px;height:33px;border-radius:17px;background:var(--blue);color:#fff;font:500 13px "Poppins",sans-serif;display:flex;align-items:center;justify-content:center}

/* footer */
.footer{position:absolute;left:0;top:3430px;width:1200px;height:696px;background:var(--navy);clip-path:polygon(0 118px,100% 0,100% 100%,0 100%);color:#fff}
.fcol{position:absolute;top:222px}
.fcol h4{font-size:17px;font-weight:500}
.fcol .rule{width:40px;height:2px;background:var(--blue);margin-top:10px}
.post .date{font-size:12px;color:#a9b2cc}
.post .title{margin-top:6px;font-size:14px;line-height:24px;font-weight:500}
.info{font-size:14px;line-height:24px}
.row{display:flex;font-size:13px;line-height:30px}
.row b{width:82px;font-weight:700;flex:none}
.field{position:absolute;background:#1b2c60;color:#a9b2cc;font-size:13px;padding:10px 14px}
.send{position:absolute;left:815px;top:3966px;width:72px;height:28px;border:1.5px solid #fff;border-radius:14px;color:#fff;font:500 12px "Poppins",sans-serif;display:flex;align-items:center;justify-content:center}
.social{display:inline-flex;gap:10px;vertical-align:middle;margin-left:22px;align-items:center}
.social i{display:block;width:12px;height:12px;background:#fff;border-radius:2px}
.bottom-rule{position:absolute;left:0;top:4018px;width:1200px;height:1px;background:#2a3a6c}
.totop{position:absolute;left:578px;top:4026px;width:44px;height:44px;border-radius:50%;background:#fff;display:flex;align-items:center;justify-content:center}
.copy{position:absolute;left:17px;top:4084px;font-size:13px;color:#fff}
.legal{position:absolute;top:4084px;font-size:12px;color:#c3c9dc}
</style>
</head>
<body>

<!-- hero -->
<header class="hero">
  <div class="brand"><span class="brand-mark"></span>TOVIN MARSK</div>
  <nav>
    <span class="nav-item" style="left:428px">Solutions</span>
    <span class="nav-item" style="left:533px">Pricing</span>
    <span class="nav-item" style="left:622px">Tovin Marsk for ▾</span>
    <span class="nav-item" style="left:780px">Customers ▾</span>
    <span class="nav-item" style="left:910px">Resources</span>
  </nav>
  <div class="login">
    <svg width="14" height="14" viewBox="0 0 14 14"><circle cx="4" cy="10" r="3" fill="none" stroke="#211b6b" stroke-width="2"/><path d="M6 8l6-6M10 4l2 2" stroke="#211b6b" stroke-width="2"/></svg>Login
  </div>
  <h1>Build Together<br>New Space for World</h1>
  <p>Sed ut perspiciatis unde omnis iste natus error sit voluptatem ccusantium doloremque laudantium, totam rem aperiam inventore.</p>
  <div class="ghost" style="left:437px;width:163px">Check Features</div>
  <div class="ghost" style="left:616px;width:146px">Explore More</div>
</header>
<div class="down"><svg width="22" height="22" viewBox="0 0 22 22"><path d="M11 3v15M5 12l6 6 6-6" fill="none" stroke="#fff" stroke-width="2.5"/></svg></div>

<!-- features -->
<section class="features">
  <div class="feature" style="left:17px">
    <svg width="70" height="70" viewBox="0 0 70 70" fill="none" stroke="#1a5df0" stroke-width="2.5"><circle cx="35" cy="38" r="28"/><path d="M17 44a19 19 0 1 1 36 0"/><path d="M35 38l12-12"/><circle cx="35" cy="38" r="3"/></svg>
    <h3>High Performance</h3>
    <p>Sed ut perspiciatis unde omnis istenor sit accusantium</p>
  </div>
  <div class="feature" style="left:316px">
    <svg width="70" height="70" viewBox="0 0 70 70" fill="none" stroke="#1a5df0" stroke-width="2.5"><circle cx="35" cy="35" r="28"/><path d="M27 32v-7a8 8 0 0 1 16 0v7"/><rect x="23" y="32" width="24" height="18" rx="2"/><path d="M35 39v5"/></svg>
    <h3>Enhance Security</h3>
    <p>Sed ut perspiciatis unde omnis istenor sit accusantium</p>
  </div>
  <div class="feature" style="left:614px">
    <svg width="70" height="70" viewBox="0 0 70 70" fill="none" stroke="#1a5df0" stroke-width="2.5"><path d="M35 6l25 9v18c0 16-11 26-25 31C21 59 10 49 10 33V15z"/><path d="M35 14l17 6v13c0 11-7 18-17 22-10-4-17-11-17-22V20z"/><circle cx="35" cy="30" r="5"/><path d="M26 44a9 7 0 0 1 18 0"/></svg>
    <h3>Spam Guard</h3>
    <p>Sed ut perspiciatis unde omnis istenor sit accusantium</p>
  </div>
  <div class="feature" style="left:911px">
    <svg width="70" height="70" viewBox="0 0 70 70" fill="none" stroke="#1a5df0" stroke-width="2.5"><path d="M12 58l28-28M18 8a10 10 0 0 0 12 14l6 6-4 4-6-6A10 10 0 0 1 12 14l6 6 4-4z"/><path d="M58 12L30 40M52 8l10 10-6 2-6-6zM14 50l6 6-6 6-6-6z"/><path d="M40 46l14 14 6-6-14-14"/></svg>
    <h3>Unbeatable Support</h3>
    <p>Sed ut perspiciatis unde omnis istenor sit accusantium</p>
  </div>
</section>

<!-- pricing -->
<div class="pricing-bg"></div>
<div class="head" style="top:1196px">
  <h2>Our Pricing Plan</h2>
  <div class="rule"></div>
  <p>There are many variations of passages of Lorem Ipsum available, but the majority have suffered alteration in some form, by injected humour</p>
</div>

<div class="plan" style="left:17px">
  <h4>Basic</h4><div class="sub">Put some text here</div><div class="rule"></div>
  <ul><li>RAM 1 GB</li><li>Core CPU 1</li><li>SSD Storage 20 GB</li><li>Transfer 1 TB</li><li>Network in 40 Gbps</li><li>Network Out 1000 Mbps</li></ul>
  <div class="price"><sup>$</sup>29<small>/m</small></div>
  <svg class="base" width="272" height="130" viewBox="0 0 272 130"><polygon points="0,10 272,0 272,130 0,130" fill="#211b6b"/></svg>
  <div class="buy">Buy Now</div>
</div>
<div class="plan" style="left:316px">
  <h4>Standard</h4><div class="sub">Put some text here</div><div class="rule"></div>
  <ul><li>RAM 1 GB</li><li>Core CPU 1</li><li>SSD Storage 20 GB</li><li>Transfer 1 TB</li><li>Network in 40 Gbps</li><li>Network Out 1000 Mbps</li></ul>
  <div class="price"><sup>$</sup>47<small>/m</small></div>
  <div class="popular">Most popular</div>
  <svg class="base" width="272" height="130" viewBox="0 0 272 130"><polygon points="0,10 272,0 272,130 0,130" fill="#211b6b"/></svg>
  <div class="buy">Buy Now</div>
</div>
<div class="plan" style="left:614px">
  <h4>Professional</h4><div class="sub">Put some text here</div><div class="rule"></div>
  <ul><li>RAM 1 GB</li><li>Core CPU 1</li><li>SSD Storage 20 GB</li><li>Transfer 1 TB</li><li>Network in 40 Gbps</li><li>Network Out 1000 Mbps</li></ul>
  <div class="price"><sup>$</sup>59<small>/m</small></div>
  <svg class="base" width="272" height="130" viewBox="0 0 272 130"><polygon points="0,10 272,0 272,130 0,130" fill="#211b6b"/></svg>
  <div class="buy">Buy Now</div>
</div>
<div class="plan" style="left:911px">
  <h4>Business</h4><div class="sub">Put some text here</div><div class="rule"></div>
  <ul><li>RAM 1 GB</li><li>Core CPU 1</li><li>SSD Storage 20 GB</li><li>Transfer 1 TB</li><li>Network in 40 Gbps</li><li>Network Out 1000 Mbps</li></ul>
  <div class="price"><sup>$</sup>180<small>/m</small></div>
  <svg class="base" width="272" height="130" viewBox="0 0 272 130"><polygon points="0,10 272,0 272,130 0,130" fill="#211b6b"/></svg>
  <div class="buy">Buy Now</div>
</div>

<!-- why choose us -->
<section class="why">
  <h2>Why Choose Us</h2>
  <p class="intro">There are many variations of passages of Lorem Ipsum available, but the majority have suffered alteration in some form.</p>
  <div class="point" style="left:17px;top:2196px"><h4>01. High Performance</h4><p>Sed ut perspiciatis unde omnis istenor sit accusantium</p></div>
  <div class="point" style="left:316px;top:2196px"><h4>02. Enhance Security</h4><p>Sed ut perspiciatis unde omnis istenor sit accusantium</p></div>
  <div class="point" style="left:17px;top:2322px"><h4>03. Spam Guard</h4><p>Sed ut perspiciatis unde omnis istenor sit accusantium</p></div>
  <div class="point" style="left:316px;top:2322px"><h4>04. Unbeatable Support</h4><p>Sed ut perspiciatis unde omnis istenor sit accusantium</p></div>
  <div class="purchase">Purchase Now</div>
  <div class="video" role="img" aria-label="Photo of business partners shaking hands over a desk with documents">
    <div class="play"><svg width="20" height="22" viewBox="0 0 20 22"><polygon points="3,2 18,11 3,20" fill="#fff"/></svg></div>
    <span>You Will Buy After Watching</span>
  </div>
</section>

<!-- clients -->
<div class="clients-bg"></div>
<div class="head" style="top:2655px">
  <h2>Our Client's Words</h2>
  <div class="rule"></div>
  <p>There are many variations of passages of Lorem Ipsum available, but the majority have suffered alteration in some form, by injected humour</p>
</div>
<div class="quote" style="left:17px">
  <div class="qmark">“</div><h4>Mara J. Penfold</h4><div class="loc">Melbourne, Australia</div>
  <p>"Lorem ipsum dolor sit amet, consectetur incididunt ut labore et dolore magna aliqua. Ut enim ad minim veniam.</p>
  <svg width="368" height="30" viewBox="0 0 368 30"><polygon points="0,30 368,0 368,30" fill="#211b6b"/></svg>
</div>
<div class="quote" style="left:416px">
  <div class="qmark">“</div><h4>Tessa C. Vane</h4><div class="loc">Sacramento, CA</div>
  <p>"Lorem ipsum dolor sit amet, consectetur incididunt ut labore et dolore magna aliqua. Ut enim ad minim veniam.</p>
  <svg width="368" height="30" viewBox="0 0 368 30"><polygon points="0,30 368,0 368,30" fill="#211b6b"/></svg>
</div>
<div class="quote" style="left:815px">
  <div class="qmark">“</div><h4>Rhun A. Callow</h4><div class="loc">Texas, USA</div>
  <p>"Lorem ipsum dolor sit amet, consectetur incididunt ut labore et dolore magna aliqua. Ut enim ad minim veniam.</p>
  <svg width="368" height="30" viewBox="0 0 368 30"><polygon points="0,30 368,0 368,30" fill="#211b6b"/></svg>
</div>
<div class="dots"><i></i><i></i><i></i></div>

<!-- newsletter -->
<section class="news">
  <h2>Sign Up Newsletter</h2>
  <p>Subscribe To Our Newsletter To Get Our Latest News, Promo Code, Special Offer's Update In Your Inbox</p>
  <div class="signup"><span>Your E-mail Address</span><b>Subscribe</b></div>
</section>

<!-- footer -->
<footer class="footer">
  <div class="fcol" style="left:17px;width:340px">
    <h4>Recent News</h4><div class="rule"></div>
    <div class="post" style="margin-top:40px"><div class="date">Posted on June 06, 2018</div><div class="title">How This Company Creates Instant Awesome Websites</div></div>
    <div class="post" style="margin-top:44px"><div class="date">Posted on May 05, 2018</div><div class="title">Crimson Loft acquires CoreNimbus to strengthen its leadership position</div></div>
    <div class="post" style="margin-top:44px"><div class="date">Posted on April 04, 2018</div><div class="title">Do People Think Your Ecommerce Business Name Is 500 error</div></div>
  </div>
  <div class="fcol" style="left:416px;width:360px">
    <h4>Contact Us</h4><div class="rule"></div>
    <p class="info" style="margin-top:34px">There are many variations of passages of Lorem Ipsum majority have suffered.</p>
    <p class="info" style="margin-top:14px">At vero eos et accusamus et iusto odio dignissimos.</p>
    <div class="row" style="margin-top:40px"><b>Telephone</b><span>: (+01) 5550-13478 , (+90) 5550-2841</span></div>
    <div class="row"><b>E-mail</b><span>: yourMail@example.com</span></div>
    <div class="row" style="line-height:22px;margin-top:4px"><b>Address</b><span>: 418 Harlow Lane, Westbrook, NY<br>&nbsp;&nbsp;14092.</span></div>
    <div class="row" style="margin-top:12px"><b style="width:auto">Follow Us</b><span class="social"><i></i><i></i><i></i><i></i><i></i><i></i></span></div>
  </div>
  <div class="fcol" style="left:812px;width:370px">
    <h4>Get In Touch</h4><div class="rule"></div>
  </div>
</footer>
<div class="field" style="left:812px;top:3699px;width:180px;height:36px">Name</div>
<div class="field" style="left:1002px;top:3699px;width:181px;height:36px">Email</div>
<div class="field" style="left:812px;top:3748px;width:371px;height:36px">Subject</div>
<div class="field" style="left:812px;top:3798px;width:371px;height:96px">Message</div>
<div class="abs" style="left:815px;top:3912px;width:368px;color:#fff;font-size:13px;line-height:22px;display:flex;gap:10px">
  <span style="flex:none;width:11px;height:11px;margin-top:5px;background:#fff"></span>
  <span>By using this form you agree with the storage and handling of your data by this website.</span>
</div>
<div class="send">Send</div>
<div class="bottom-rule"></div>
<div class="totop"><svg width="16" height="16" viewBox="0 0 16 16"><path d="M8 14V3M3 7l5-5 5 5" fill="none" stroke="#0e1e4f" stroke-width="2.2"/></svg></div>
<div class="copy">Copyright © 2018 Tovin Marsk. All Rights Reserved.</div>
<div class="legal" style="left:815px">About</div>
<div class="legal" style="left:878px">Affiliate</div>
<div class="legal" style="left:950px">Privacy Policy</div>
<div class="legal" style="left:1060px">Terms &amp; Conditions</div>

</body>
</html>
```